Steady Valve Systems

I need a business card with the attached logo.
The second page I have attached is what we are looking for. We want doubles sided. We would like the blues fading and the logo on the back.

Industry/Entity Type

Business

```html
<!DOCTYPE html>
<html lang="en">
<head>
<meta charset="utf-8">
<title>Steady Valve Systems – Business Card</title>
<link rel="stylesheet" href="https://fonts.googleapis.com/css2?family=Exo+2:wght@400;500;700&display=swap">
<style>
  :root {
    --brand-blue: #003b8e;
    --brand-blue-dark: #002a6a;
    --band-grey: #9a9ca0;
    --ink: #2b2b2b;
    --ink-soft: #444649;
    --card: #ffffff;
    --stage: #e4e5e7;
  }
  * { box-sizing: border-box; margin: 0; padding: 0; }
  html, body {
    width: 1200px;
    height: 900px;
    overflow: hidden;
    background: var(--stage);
    font-family: "Exo 2", sans-serif;
  }
  .card {
    position: absolute;
    left: 110px;
    top: 170px;
    width: 980px;
    height: 560px;
    background: var(--card);
    box-shadow: 0 10px 30px rgba(0,0,0,0.15);
    overflow: hidden;
  }
  .card__swoosh {
    position: absolute;
    inset: 0;
    width: 100%;
    height: 100%;
  }
  .brand {
    position: absolute;
    left: 100px;
    top: 262px;
    display: flex;
    align-items: center;
    gap: 14px;
  }
  .brand__mark {
    width: 20px;
    height: 20px;
    background: var(--brand-blue);
  }
  .brand__name {
    font-weight: 700;
    font-size: 36px;
    letter-spacing: 2px;
    color: var(--brand-blue);
    text-transform: uppercase;
    white-space: nowrap;
  }
  .person {
    position: absolute;
    right: 90px;
    top: 56px;
    text-align: right;
  }
  .person__name {
    font-weight: 500;
    font-size: 27px;
    letter-spacing: 1.5px;
    color: var(--ink);
    text-transform: uppercase;
  }
  .person__title {
    font-size: 19px;
    color: var(--ink-soft);
    margin-top: 2px;
  }
  .contacts {
    position: absolute;
    right: 90px;
    top: 140px;
    list-style: none;
  }
  .contacts__item {
    display: flex;
    justify-content: flex-end;
    align-items: center;
    gap: 12px;
    font-size: 17px;
    letter-spacing: 1px;
    color: var(--ink);
    height: 30px;
    white-space: nowrap;
  }
  .contacts__icon {
    width: 18px;
    height: 18px;
    fill: var(--ink);
    flex: none;
  }
  .address {
    position: absolute;
    left: 48px;
    bottom: 24px;
    color: #ffffff;
    font-size: 24px;
    font-style: normal;
    line-height: 1.3;
    letter-spacing: 1px;
  }
</style>
</head>
<body>
  <main class="card">
    <svg class="card__swoosh" viewBox="0 0 980 560" aria-hidden="true">
      <defs>
        <linearGradient id="blueFade" x1="0" y1="1" x2="1" y2="0">
          <stop offset="0" stop-color="#002a6a"/>
          <stop offset="0.6" stop-color="#003b8e"/>
          <stop offset="1" stop-color="#0a4aa3"/>
        </linearGradient>
      </defs>
      <path class="band band--grey" fill="#9a9ca0"
            d="M500,462 C760,400 900,330 980,280 L980,330 C860,390 720,440 500,462 Z"/>
      <path class="band band--blue" fill="url(#blueFade)"
            d="M0,475 C380,485 770,420 980,330 L980,560 L0,560 Z"/>
      <rect class="corner-tab" x="905" y="0" width="75" height="28" fill="#9a9ca0"/>
    </svg>

    <div class="brand">
      <span class="brand__mark"></span>
      <span class="brand__name">Steady Valve Systems</span>
    </div>

    <div class="person">
      <p class="person__name">Daniel Mercer</p>
      <p class="person__title">Managing Director</p>
    </div>

    <ul class="contacts">
      <li class="contacts__item">012 555 0147
        <svg class="contacts__icon" viewBox="0 0 24 24"><path d="M6.6 10.8a15 15 0 0 0 6.6 6.6l2.2-2.2c.3-.3.7-.4 1-.2 1.1.4 2.3.6 3.6.6.6 0 1 .4 1 1V20c0 .6-.4 1-1 1C10.6 21 3 13.4 3 4c0-.6.4-1 1-1h3.5c.6 0 1 .4 1 1 0 1.3.2 2.5.6 3.6.1.3 0 .7-.2 1z"/></svg>
      </li>
      <li class="contacts__item">012 555 0148
        <svg class="contacts__icon" viewBox="0 0 24 24"><path d="M7 2h10a2 2 0 0 1 2 2v16a2 2 0 0 1-2 2H7a2 2 0 0 1-2-2V4a2 2 0 0 1 2-2zm0 3v13h10V5z"/></svg>
      </li>
      <li class="contacts__item">012 555 0149
        <svg class="contacts__icon" viewBox="0 0 24 24"><path d="M7 3h8l3 3v4H7zM4 11h16a1 1 0 0 1 1 1v6h-3v3H6v-3H3v-6a1 1 0 0 1 1-1zm4 6v2h8v-2z"/></svg>
      </li>
      <li class="contacts__item">info@steadyvalve.com
        <svg class="contacts__icon" viewBox="0 0 24 24"><path d="M3 5h18v14H3zm2 2v.5l7 4.5 7-4.5V7zm0 2.8V17h14V9.8l-7 4.5z"/></svg>
      </li>
      <li class="contacts__item">www.steadyvalve.com
        <svg class="contacts__icon" viewBox="0 0 24 24"><path d="M12 2a10 10 0 1 0 0 20 10 10 0 0 0 0-20zm6.9 9h-3a15 15 0 0 0-1.3-5.7A8 8 0 0 1 18.9 11zM12 4c.9 1.2 1.7 3.6 1.9 7h-3.8c.2-3.4 1-5.8 1.9-7zM9.4 5.3A15 15 0 0 0 8.1 11h-3a8 8 0 0 1 4.3-5.7zM5.1 13h3a15 15 0 0 0 1.3 5.7A8 8 0 0 1 5.1 13zM12 20c-.9-1.2-1.700-3.6-1.9-7h3.8c-.2 3.4-1 5.8-1.9 7zm2.6-1.3a15 15 0 0 0 1.3-5.7h3a8 8 0 0 1-4.3 5.7z"/></svg>
      </li>
    </ul>

    <address class="address">
      Unit 12, 4th floor,<br>Harbor Road East
    </address>
  </main>
</body>
</html>
```